Rocket business card

Modern business card design, use of color is good with clean space too.

Things to include on card:

Quote: I add fuel to your optometry practice

- Eyewear Sales
- Admin Duties
- Revenue Collection
- Leadership
- Tech Adoption
- COGS Reduction
- Product Sourcing
-Medical Growth

Dalton Vessey, CEO
Glint Harbor
Text Me! 847-302-1964
dalton@glintharbor.example

```html
<!DOCTYPE html>
<html lang="en">
<head>
<meta charset="utf-8">
<title>Glint Harbor — Business Card</title>
<link rel="stylesheet" href="https://fonts.googleapis.com/css2?family=Montserrat:wght@300;500&family=Oswald:wght@600&family=Open+Sans:wght@300;400&display=swap">
<style>
  :root {
    --page-bg: #2a2a2a;
    --card-bg: #1c1c1c;
    --edge-orange: #f26522;
    --accent-orange: #e8702a;
    --text-white: #f4f4f4;
    --text-grey: #c9c9c9;
  }
  * { box-sizing: border-box; margin: 0; padding: 0; }
  html, body {
    width: 1200px;
    height: 895px;
    overflow: hidden;
    background: var(--page-bg);
  }
  .sheet {
    width: 1200px;
    height: 895px;
    display: flex;
    flex-direction: column;
    align-items: center;
    justify-content: center;
    gap: 40px;
  }
  .card {
    position: relative;
    width: 672px;
    height: 384px;
    background: var(--card-bg);
    border-radius: 18px;
    border-bottom: 5px solid var(--edge-orange);
    box-shadow: 0 14px 30px rgba(0,0,0,0.55);
    overflow: hidden;
  }

  /* Front */
  .card-front {
    display: flex;
    flex-direction: column;
    align-items: center;
    justify-content: center;
    gap: 34px;
  }
  .brand-lockup {
    display: flex;
    align-items: center;
    gap: 22px;
  }
  .brand-dot {
    width: 78px;
    height: 78px;
    border-radius: 50%;
    background: var(--accent-orange);
  }
  .brand-name {
    font-family: "Montserrat", sans-serif;
    font-weight: 300;
    font-size: 46px;
    letter-spacing: 3px;
    text-transform: uppercase;
    color: var(--text-white);
  }
  .services {
    font-family: "Montserrat", sans-serif;
    font-weight: 500;
    font-size: 14.5px;
    line-height: 1.55;
    letter-spacing: 0.8px;
    color: var(--text-white);
    text-align: center;
  }

  /* Back */
  .card-back .identity {
    position: absolute;
    left: 70px;
    top: 118px;
    display: flex;
    align-items: center;
  }
  .person-name {
    font-family: "Oswald", sans-serif;
    font-weight: 600;
    font-size: 44px;
    letter-spacing: 1px;
    text-transform: uppercase;
    color: var(--text-white);
  }
  .divider {
    width: 1.5px;
    height: 74px;
    background: var(--text-white);
    margin: 0 24px;
  }
  .contact {
    font-family: "Open Sans", sans-serif;
    font-weight: 300;
    font-size: 17px;
    line-height: 1.5;
    color: var(--text-grey);
  }
  .contact-label { color: var(--accent-orange); }
  .back-wordmark {
    position: absolute;
    right: 60px;
    bottom: 52px;
    font-family: "Montserrat", sans-serif;
    font-weight: 300;
    font-size: 24px;
    letter-spacing: 2px;
    text-transform: uppercase;
    color: var(--text-white);
  }
</style>
</head>
<body>
<main class="sheet">
  <section class="card card-front" aria-label="Card front">
    <div class="brand-lockup">
      <span class="brand-dot" aria-hidden="true"></span>
      <span class="brand-name">Glint Harbor</span>
    </div>
    <p class="services">
      Eyewear Sales - Admin Duties - Revenue Collection - Leadership<br>
      Tech Adoption - COGS Reduction - Product Sourcing - Medical Growth
    </p>
  </section>

  <section class="card card-back" aria-label="Card back">
    <div class="identity">
      <h1 class="person-name">Dalton Vessey, CEO</h1>
      <span class="divider" aria-hidden="true"></span>
      <div class="contact">
        <p><span class="contact-label">Text Me!</span> 847-302-1964</p>
        <p><span class="contact-label">Email:</span> dalton@glintharbor.example</p>
      </div>
    </div>
    <p class="back-wordmark">Glint Harbor</p>
  </section>
</main>
</body>
</html>
```